The Keystone Listing Guide

I have a book that I need a cover for. The main title will be "The Maplecrest Keystone Listing Guide" and the secondary title will be "27 ways to close with ease" With the design, I think I'd like to include some sort of blueprint drawing with drafting like font. But the blueprint drawing isn't a requirement.

Target Market(s)

Home/property sellers

Industry/Entity Type

Real Estate

Font styles to use
Serif
Sans Serif
Other font styles liked:
• Architect type handwriting

```html
<!DOCTYPE html>
<html lang="en">
<head>
<meta charset="utf-8">
<title>The Maplecrest Keystone Listing Guide</title>
<link rel="stylesheet" href="https://fonts.googleapis.com/css2?family=Open+Sans:wght@600&family=Noto+Serif:ital,wght@0,600;1,600&display=swap">
<style>
  :root {
    --cover-light: #f8ebc0;
    --cover-base: #f1dc9e;
    --cover-deep: #e8cf88;
    --gold-light: #f4dc7a;
    --gold-mid: #c99a2e;
    --gold-dark: #8a5f12;
    --band-dark: #9c6e1c;
    --band-light: #f3e08e;
    --ink: #1a1407;
    --art-gold: #b8862a;
    --art-white: #fbf7ec;
  }
  * { margin: 0; padding: 0; box-sizing: border-box; }
  html, body {
    width: 960px;
    height: 1200px;
    overflow: hidden;
  }
  body {
    background: radial-gradient(ellipse at 50% 35%, var(--cover-light) 0%, var(--cover-base) 55%, var(--cover-deep) 100%);
    position: relative;
  }
  .cover { position: absolute; inset: 0; }

  .title {
    position: absolute;
    top: 38px;
    left: 0;
    right: 0;
    display: flex;
    flex-direction: column;
    align-items: center;
    text-transform: uppercase;
  }
  .title-line {
    display: block;
    font-family: "Open Sans", sans-serif;
    font-weight: 600;
    font-size: 104px;
    line-height: 118px;
    letter-spacing: -1px;
    background: linear-gradient(180deg, var(--gold-light) 0%, var(--gold-mid) 55%, var(--gold-dark) 100%);
    -webkit-background-clip: text;
    background-clip: text;
    color: transparent;
    filter: drop-shadow(2px 3px 2px rgba(90, 60, 10, 0.45));
  }
  .title-line--accent {
    font-family: "Noto Serif", serif;
    font-size: 118px;
    line-height: 136px;
    letter-spacing: 2px;
  }

  .house-art {
    position: absolute;
    top: 648px;
    left: 250px;
    width: 460px;
    height: 232px;
    border-radius: 6px 6px 0 0;
    background: linear-gradient(180deg, var(--art-gold) 0%, #d9b869 40%, var(--art-white) 75%, #efe6cf 100%);
  }

  .subtitle-band {
    position: absolute;
    top: 880px;
    left: 0;
    right: 0;
    height: 86px;
    display: flex;
    align-items: center;
    justify-content: center;
    background: linear-gradient(90deg, var(--band-dark) 0%, var(--gold-mid) 25%, var(--band-light) 50%, var(--gold-mid) 75%, var(--band-dark) 100%);
  }
  .subtitle {
    font-family: "Noto Serif", serif;
    font-style: italic;
    font-weight: 600;
    font-size: 36px;
    color: var(--ink);
  }
</style>
</head>
<body>
  <main class="cover">
    <h1 class="title">
      <span class="title-line">The</span>
      <span class="title-line">Maplecrest</span>
      <span class="title-line">Keystone</span>
      <span class="title-line">Listing</span>
      <span class="title-line title-line--accent">Guide</span>
    </h1>
    <div class="house-art" role="img" aria-label="Illustration of two white houses with black roofs in front of a larger gold house"></div>
    <div class="subtitle-band">
      <p class="subtitle">27 ways to close with ease</p>
    </div>
  </main>
</body>
</html>
```